regPersonal Trainer Flyer Design

Reason: I have been very busy with other work and would like to extend the deadline to offer designers the chance to edit and improve designs with my help. Thank you for all the designs that have been sent so far.

```html
<!DOCTYPE html>
<html lang="en">
<head>
<meta charset="utf-8">
<title>Personal Trainer Flyer</title>
<link href="https://fonts.googleapis.com/css2?family=Baloo+2:wght@600;700&family=Oswald:wght@500&family=Comic+Neue:wght@400&family=Ubuntu:wght@400&display=swap" rel="stylesheet">
<style>
  :root {
    --backdrop: #2b2b2b;
    --flyer-deep: #0b4575;
    --flyer-mid: #1a6aa6;
    --flyer-light: #2b84c4;
    --swirl-glow: rgba(120, 170, 230, 0.35);
    --panel-light: #5aa6e6;
    --panel-dark: #2f7cc4;
    --panel-edge: rgba(255, 255, 255, 0.55);
    --band-blue: #2f86d0;
    --curl-light: #ffffff;
    --curl-shade: #d9d9d9;
    --offer-orange: #f5a21e;
    --white: #ffffff;
    --ink: #0d1b2a;
  }
  * { margin: 0; padding: 0; box-sizing: border-box; }
  html, body { width: 1200px; height: 1000px; overflow: hidden; background: var(--backdrop); }
  .canvas { position: relative; width: 1200px; height: 1000px; }
  .flyer {
    position: absolute; left: 30px; top: 97px; width: 1142px; height: 808px;
    background: radial-gradient(ellipse at 40% 45%, var(--flyer-light) 0%, var(--flyer-mid) 45%, var(--flyer-deep) 100%);
    overflow: hidden;
  }
  .swirl { position: absolute; }
  .swirl-top-left {
    left: 0; top: 0; width: 420px; height: 260px;
    background: radial-gradient(ellipse at 30% 20%, var(--swirl-glow) 0%, rgba(120,170,230,0) 70%);
  }
  .swirl-right {
    left: 940px; top: 480px; width: 202px; height: 200px;
    background: radial-gradient(ellipse at 70% 50%, var(--swirl-glow) 0%, rgba(120,170,230,0) 70%);
  }
  .text-panel {
    position: absolute; left: 728px; top: 0; width: 362px; height: 450px;
    background: linear-gradient(90deg, var(--panel-dark), var(--panel-light) 50%, var(--panel-dark));
    border-left: 2px solid var(--panel-edge); border-right: 2px solid var(--panel-edge);
  }
  .text-panel-foot {
    position: absolute; left: 708px; top: 445px; width: 396px; height: 83px;
    background: linear-gradient(90deg, var(--panel-dark), var(--panel-light) 50%, var(--panel-dark));
    border: 1.5px solid var(--panel-edge);
  }
  .offer-band {
    position: absolute; left: 205px; top: 253px; width: 320px; height: 170px; background: var(--band-blue);
  }
  .band-end { position: absolute; top: 242px; width: 178px; height: 184px; }
  .band-end-left { left: 30px; background: linear-gradient(90deg, var(--curl-light), var(--curl-light) 60%, var(--curl-shade)); }
  .band-end-right { left: 523px; background: linear-gradient(90deg, var(--curl-shade), var(--curl-light) 30%, var(--curl-light)); }
  .headline {
    position: absolute; font-family: "Baloo 2", "Trebuchet MS", sans-serif; font-weight: 700;
    color: var(--white); font-size: 51px; line-height: 1; text-shadow: 1px 2px 3px rgba(0,0,0,.35);
    white-space: nowrap;
  }
  .headline-one { left: 38px; top: 86px; }
  .headline-two { left: 177px; top: 141px; letter-spacing: 0.4px; }
  .offer {
    position: absolute; left: 205px; top: 293px; width: 320px; text-align: center;
    font-family: "Oswald", "Arial Narrow", sans-serif; font-weight: 500; color: var(--offer-orange);
    font-size: 37px; line-height: 47px;
  }
  .needs {
    position: absolute; left: 743px; top: 57px; width: 320px; list-style: none;
    font-family: "Comic Neue", "Comic Sans MS", cursive; font-size: 15.5px; color: var(--ink); line-height: 18px;
  }
  .needs li { position: absolute; left: 0; padding-left: 23px; width: 320px; white-space: nowrap; }
  .needs li::before {
    content: ""; position: absolute; left: 0; top: 1px; width: 0; height: 0;
    border-top: 9px solid transparent; border-bottom: 9px solid transparent; border-left: 14px solid var(--white);
  }
  .contact-title {
    position: absolute; left: 166px; top: 481px; width: 376px; text-align: center; white-space: nowrap;
    font-family: "Ubuntu", Arial, sans-serif; font-size: 29px; letter-spacing: 0.6px; color: var(--white);
    text-decoration: underline; text-underline-offset: 6px; text-decoration-thickness: 2px;
  }
  .contact-line {
    position: absolute; left: 38px; font-family: "Ubuntu", Arial, sans-serif; font-size: 24px;
    letter-spacing: 0.5px; color: var(--white); white-space: nowrap;
  }
  .contact-line .sep { font-weight: 700; margin: 0 7px; }
  .contact-role { top: 540px; }
  .contact-reach { top: 585px; }
  .photo-strip {
    position: absolute; left: 22px; top: 645px; width: 1095px; height: 143px; background: var(--white);
  }
  .photo { position: absolute; top: 10px; width: 198px; height: 124px; }
  .photo-1 { left: 17px; background: linear-gradient(135deg, #6b7b86, #2f3a42); }
  .photo-2 { left: 233px; background: linear-gradient(135deg, #c9c4c0, #8a6a5c); }
  .photo-3 { left: 448px; background: linear-gradient(135deg, #b23a2e, #3a3a44); }
  .photo-4 { left: 663px; background: linear-gradient(135deg, #8a4a36, #3b3b3b); }
  .photo-5 { left: 879px; background: linear-gradient(135deg, #e6e4e0, #4a6f8f); }
</style>
</head>
<body>
<div class="canvas">
  <div class="flyer">
    <div class="swirl swirl-top-left" role="img" aria-label="Faint flowing line swirl decoration"></div>
    <div class="swirl swirl-right" role="img" aria-label="Faint flowing line swirl decoration"></div>

    <div class="text-panel" role="img" aria-label="Unrolled paper scroll panel"></div>
    <div class="text-panel-foot" role="img" aria-label="Rolled lower end of the paper scroll"></div>

    <div class="offer-band"></div>
    <div class="band-end band-end-left" role="img" aria-label="Curled white paper ribbon end"></div>
    <div class="band-end band-end-right" role="img" aria-label="Curled white paper ribbon end"></div>

    <div class="headline headline-one">Achieving Your Fitness</div>
    <div class="headline headline-two">Goals Just Got Easier...!!</div>

    <div class="offer">*Introductory offer<br>One Free Session*</div>

    <ul class="needs">
      <li style="top:0">Need a personal trainer to&nbsp; improving<br>Fitness, Health, Posture, or Recover<br>from an Injury or complete a Marathon??</li>
      <li style="top:70px">Lacking motivation?</li>
      <li style="top:108px">Not achieving your goals?</li>
      <li style="top:147px">Bored of the gym?</li>
      <li style="top:187px">You're never too old</li>
      <li style="top:224px">Need help?</li>
      <li style="top:263px">I can help improve your health and<br>well-being</li>
      <li style="top:316px">Training can be at your home</li>
    </ul>

    <div class="contact-title">-Feel Free To Contact Me-</div>
    <div class="contact-line contact-role">Profession :&nbsp; Personal Trainer<span class="sep">|</span>Name : Sam Keller</div>
    <div class="contact-line contact-reach">Mobile Number : 07700900123<span class="sep">|</span>email : samkeller@example.co.uk</div>

    <div class="photo-strip">
      <div class="photo photo-1" role="img" aria-label="Trainer working with suspension straps in a gym"></div>
      <div class="photo photo-2" role="img" aria-label="Trainer guiding a client through a barbell exercise"></div>
      <div class="photo photo-3" role="img" aria-label="Client doing suspension strap rows with trainer"></div>
      <div class="photo photo-4" role="img" aria-label="Trainer lifting a barbell against a brick wall"></div>
      <div class="photo photo-5" role="img" aria-label="Trainer holding boxing pads for a client"></div>
    </div>
  </div>
</div>
</body>
</html>
```